Business card like design

Hello we need a business card like design, not with personal info. But with info from our shop, like address, phone, street, email, facebook .....
This cards we put in the box when we send out the orders......
Target Market(s)
We sell cheap sunglasses, our customers are mainly young adults, that like going to parties
Industry/Entity Type
Business

```html
<!DOCTYPE html>
<html lang="en">
<head>
<meta charset="utf-8">
<title>Bright Shades – shop card</title>
<link rel="stylesheet" href="https://fonts.googleapis.com/css2?family=Play:wght@400;700&display=swap">
<style>
  :root {
    --orange: #f7941d;
    --orange-deep: #e9830f;
    --white: #ffffff;
    --ink: #1c1c1c;
    --ink-soft: #fff8ee;
    --backdrop: #ece7e0;
    --shadow: rgba(0, 0, 0, 0.22);
  }
  * { box-sizing: border-box; margin: 0; padding: 0; }
  html, body {
    width: 1200px;
    height: 1023px;
    overflow: hidden;
    background: var(--backdrop);
    font-family: "Play", "Trebuchet MS", sans-serif;
  }
  .sheet {
    position: relative;
    width: 1200px;
    height: 1023px;
    display: flex;
    align-items: center;
    justify-content: center;
    gap: 50px;
  }
  .card {
    position: relative;
    width: 520px;
    height: 320px;
    background: var(--white);
    box-shadow: 0 8px 24px var(--shadow);
    overflow: hidden;
  }

  /* Back side: contact info band over brand area */
  .card--back .contact-band {
    position: absolute;
    inset: 0 0 auto 0;
    height: 150px;
    background: var(--orange);
    padding: 22px 0 0 40px;
    color: var(--ink-soft);
  }
  .contact-band .halo {
    position: absolute;
    right: 40px;
    top: 20px;
    width: 110px;
    height: 110px;
    border-radius: 50%;
    background: var(--orange-deep);
    opacity: 0.55;
  }
  .contact-list { list-style: none; position: relative; }
  .contact-item {
    display: flex;
    align-items: flex-start;
    gap: 10px;
    font-size: 14px;
    line-height: 17px;
    margin-bottom: 4px;
  }
  .contact-item svg { flex: 0 0 14px; margin-top: 2px; }

  .brand {
    position: absolute;
    display: flex;
    align-items: center;
    justify-content: center;
    gap: 14px;
  }
  .card--back .brand { inset: 150px 0 0 0; }
  .card--front .brand { inset: 0 18px 0 0; }
  .brand-dot {
    border-radius: 50%;
    background: var(--orange);
  }
  .card--back .brand-dot { width: 46px; height: 46px; }
  .card--front .brand-dot { width: 64px; height: 64px; }
  .brand-name {
    font-weight: 700;
    color: var(--ink);
    letter-spacing: 0.5px;
  }
  .card--back .brand-name { font-size: 30px; }
  .card--front .brand-name { font-size: 40px; }

  /* Front side: edge stripe */
  .card--front .edge-stripe {
    position: absolute;
    top: 0; right: 0; bottom: 0;
    width: 18px;
    background: var(--orange);
  }
</style>
</head>
<body>
<main class="sheet">

  <section class="card card--back" aria-label="Card back">
    <div class="contact-band">
      <div class="halo" aria-hidden="true"></div>
      <ul class="contact-list">
        <li class="contact-item">
          <svg width="14" height="14" viewBox="0 0 14 14" aria-hidden="true"><path d="M7 1a4 4 0 0 1 4 4c0 3-4 8-4 8S3 8 3 5a4 4 0 0 1 4-4z" fill="#fff8ee"/><circle cx="7" cy="5" r="1.5" fill="#f7941d"/></svg>
          <span>Zonnelaan 12<br>4811 AB Breda<br>Nederland</span>
        </li>
        <li class="contact-item">
          <svg width="14" height="14" viewBox="0 0 14 14" aria-hidden="true"><path d="M3 1l2.5 3-1.5 1.5c.8 1.8 2.2 3.2 4 4L9.5 8 13 10.5 11.5 13C6 13 1 8 1 2.5z" fill="#fff8ee"/></svg>
          <span>0031 10 555 01 23</span>
        </li>
        <li class="contact-item">
          <svg width="14" height="14" viewBox="0 0 14 14" aria-hidden="true"><rect x="1" y="3" width="12" height="8" fill="#fff8ee"/><path d="M1 3l6 5 6-5" fill="none" stroke="#f7941d" stroke-width="1.2"/></svg>
          <span>info@BrightShades.nl</span>
        </li>
        <li class="contact-item">
          <svg width="14" height="14" viewBox="0 0 14 14" aria-hidden="true"><circle cx="7" cy="7" r="6" fill="#fff8ee"/></svg>
          <span>social.example/brightshades</span>
        </li>
      </ul>
    </div>
    <div class="brand">
      <span class="brand-dot" aria-hidden="true"></span>
      <span class="brand-name">brightshades.nl</span>
    </div>
  </section>

  <section class="card card--front" aria-label="Card front">
    <div class="brand">
      <span class="brand-dot" aria-hidden="true"></span>
      <span class="brand-name">brightshades.nl</span>
    </div>
    <div class="edge-stripe" aria-hidden="true"></div>
  </section>

</main>
</body>
</html>
```